A new website for Electrical Contractor Business

We are looking for a unique and new WordPress website design which would include 5 Pages - Home Page, Meet the Team, Our Services, Our Projects and Contact Us page.

The global theme for the website needs to be professional but simple to navigate as we cater for both business and home owner customers.

Our core business service is targeted around lighting from single room decorative to large office so the theme should incorporate this in some way.

The home page should include;
Our business logo, Contact number, Email address, small Image rotation box - Highlighting pervious projectsText box - With welcome message, twitter feed news reel/Customer feed back box.

I would also like to see a 2 boxes for the separate customer types we services. Business and Home Owner. each box will have a small image with a small text description with a link to the area of the services page relevant to that customer type.

Meet the team page -This will be introducing potential customers to the team so I would like it to include for each team member. Something like a small image and text area which will introduce an outline of the team members skills and abilities.

Our Services page This page will be outlining the different services on offer to the both customer types business and homeowner. Each service should have an image with text description of the service would good here.

Our projects page-Will include images of pervious projects and work we have completed along with a text area for the project description/ outliner.

Contact Us page - Should include a contact form which should include an option for the customer to quest us to call them back, also a selection box for them to inform us our how they found our details would be good.

Colour - The theme colours can be taken from the logo or feel free to impress with your own imagination.

Remember we are looking for a website that will interest our customers enough to except our services or be drawn further into the website.. So call to action links to other areas of the site/ contact page are welcome

Target Market(s)

Business - Office, warehousing and Large Store - lighting and Power
Home owner lighting and power

Coding

Coded - Design and coding required

Number of Pages Required

5+ page

Font styles to use
Serif
Sans Serif

Colors

Designer to choose colors to be used in the design.

Requirements
Must have
• Logo integrated into the website design - i.e. website colours which allow the logo to blend into the design.
Nice to have
• Custom but professional theme catering to business customers, but also show that we do provide services to home owners too.
Should not have
• Sorry am not interested in one oversized block image on rotation covering half the home page.. Images will be needed but not a single block over sized frame with not text, shape. Please use your imagination when considering this design

```html
<!DOCTYPE html>
<html lang="en">
<head>
<meta charset="utf-8">
<title>Voltwise Electrical</title>
<link href="https://fonts.googleapis.com/css2?family=Poppins:wght@400;500;600&family=Saira:wght@600;700&display=swap" rel="stylesheet">
<style>
:root{
  --navy:#1c2f5e;
  --navy-deep:#17284f;
  --orange:#e9672a;
  --orange-soft:#e57441;
  --ink:#2b2b2b;
  --grey-band:#f1f1f1;
  --white:#ffffff;
}
*{margin:0;padding:0;box-sizing:border-box}
html,body{width:1200px;height:2564px;overflow:hidden}
body{position:relative;font-family:"Poppins",sans-serif;color:var(--ink);background:var(--white)}
.abs{position:absolute}
.head-font{font-family:"Saira",sans-serif}

/* hero */
.hero{left:0;top:0;width:1200px;height:420px;background:linear-gradient(100deg,#4c4a43 0%,#3b4258 45%,#253a6c 100%)}
.top-bar{left:0;top:0;width:1200px;height:33px;background:rgba(23,40,79,.85);font-size:13px;color:var(--white)}
.top-bar .lic{left:146px;top:8px}
.top-bar .abn{left:276px;top:8px}
.top-bar em{font-style:normal;color:var(--orange)}
.top-bar .divider{left:256px;top:0;width:1px;height:33px;background:rgba(255,255,255,.3)}
.top-phone{left:922px;top:0;width:136px;height:33px;background:var(--orange);color:var(--white);font-size:16px;font-weight:500;display:flex;align-items:center;justify-content:center;gap:6px}
.header{left:0;top:33px;width:1200px;height:87px;background:rgba(255,255,255,.82)}
.brand{left:140px;top:52px;display:flex;align-items:center;gap:10px;font-weight:600;font-size:24px;color:var(--navy);letter-spacing:1px}
.brand .dot{width:46px;height:46px;border-radius:50%;border:4px solid var(--navy)}
.nav{left:500px;top:71px;display:flex;font-size:15px;color:var(--ink)}
.nav span{display:block}
.nav .active{color:var(--orange)}
.hero-title{right:144px;top:166px;text-align:right;color:var(--white);font-weight:600;font-size:25px;line-height:34px}
.hero-cta{left:882px;top:284px;width:174px;height:31px;border-radius:16px;background:var(--orange);color:var(--white);font-size:15px;display:flex;align-items:center;gap:8px;padding-left:6px}
.mini-dot{width:26px;height:26px;border-radius:50%;border:2px solid var(--white)}
.hero-arrow{top:254px;width:32px;height:28px;background:rgba(30,30,30,.8);display:flex;align-items:center;justify-content:center}

/* welcome */
.welcome-title{left:143px;top:505px;font-size:29px;font-weight:700;color:var(--navy);letter-spacing:.5px}
.welcome-text{left:143px;top:565px;width:545px;font-size:13.5px;line-height:25.5px;color:#333}
.pill{left:141px;top:758px;width:178px;height:33px;border-radius:17px;background:var(--navy);color:var(--white);font-size:14.5px;display:flex;align-items:center;gap:8px;padding-left:4px}
.welcome-visual{left:733px;top:418px;width:370px;height:370px;border-radius:50%;background:linear-gradient(135deg,#c9ccd3 0%,#4a5f92 55%,#22396b 100%)}

/* audience cards */
.card{top:880px;height:227px;display:flex}
.card .photo{width:218px;height:227px}
.card .body{width:221px;height:227px;color:var(--white);text-align:center;padding-top:30px}
.card .body h3{font-family:"Saira",sans-serif;font-weight:600;font-size:18px;margin-top:8px}
.card .body p{font-size:12.3px;line-height:20px;padding:0 14px;margin-top:4px}
.card-badge{left:575px;top:968px;width:46px;height:46px;border-radius:50%;background:var(--white);border:4px solid var(--navy)}

/* projects */
.projects{left:0;top:1193px;width:1200px;height:533px;background:var(--navy)}
.section-title{width:1200px;left:0;text-align:center;font-family:"Saira",sans-serif;font-weight:700;letter-spacing:.5px}
.filters{left:0;top:1348px;width:1200px;display:flex;justify-content:center;gap:14px}
.filters span{height:34px;padding:0 16px;background:#efefef;color:var(--ink);font-family:"Saira",sans-serif;font-weight:600;font-size:17px;display:flex;align-items:center}
.filters .on{background:var(--orange);color:var(--white)}
.tile{top:1424px;width:219px;height:176px}
.tile .cap{position:absolute;left:0;bottom:0;width:100%;height:38px;background:rgba(233,103,42,.9);color:var(--white);font-family:"Saira",sans-serif;font-weight:600;font-size:15px;display:flex;align-items:center;justify-content:center}

/* testimonial */
.review{left:236px;top:1673px;width:728px;height:190px;background:var(--white);border-top:3px solid var(--orange-soft);box-shadow:0 6px 18px rgba(0,0,0,.14)}
.reviewer{left:270px;top:1708px;width:112px;height:112px;border-radius:50%;border:5px solid var(--white);box-shadow:0 0 0 2px #ddd;background:linear-gradient(160deg,#a57b60,#3e5a86)}
.quote-text{left:494px;top:1700px;width:420px;font-size:14px;line-height:26px;color:#222}
.quote-name{left:496px;top:1786px;font-size:12.5px;font-weight:600}
.round-arrow{top:1752px;width:34px;height:34px;border-radius:50%;border:1px solid #ddd;background:var(--white);display:flex;align-items:center;justify-content:center}
.more-link{left:0;top:1888px;width:1200px;display:flex;justify-content:center;align-items:center;gap:8px;font-size:14px;font-weight:500}

/* why */
.why{left:0;top:1984px;width:1200px;height:262px;background:var(--grey-band)}
.why-copy{left:0;width:1200px;text-align:center;font-size:16px;color:#333}
.why-link{left:0;top:2163px;width:1200px;text-align:center;font-size:15px;color:var(--navy)}
.why-link span{border-bottom:1px solid var(--navy);padding-bottom:2px}

/* footer */
.footer{left:0;top:2246px;width:1200px;height:273px;background:var(--orange-soft);color:var(--white)}
.col-title{top:2313px;font-size:15.5px;font-weight:600;padding-bottom:8px;border-bottom:1px solid rgba(255,255,255,.35)}
.links{left:146px;top:2354px;font-size:12.5px;line-height:26px}
.contact-row{display:flex;gap:12px;align-items:flex-start;font-size:12.5px;line-height:18px}
.feed{left:628px;top:2354px;width:240px;font-size:12.5px;line-height:19px}
.footer-brand{left:900px;top:2380px;display:flex;align-items:center;gap:12px;font-weight:600;font-size:24px}
.footer-brand .dot{width:46px;height:46px;border-radius:50%;border:4px solid var(--white)}
.bottom-bar{left:0;top:2519px;width:1200px;height:45px;background:var(--navy);color:var(--white);font-size:12px}
.social{top:15px;width:14px;height:14px;border-radius:50%;background:var(--white)}
</style>
</head>
<body>

<!-- hero -->
<div class="abs hero" role="img" aria-label="Hanging pendant lamps and exposed bulbs in a dim room"></div>
<svg class="abs" style="left:0;top:370px" width="1200" height="60" viewBox="0 0 1200 60">
  <path d="M0 32 C300 60 600 10 800 10 C980 10 1100 24 1200 14 L1200 60 L0 60 Z" fill="#ffffff"/>
  <path d="M0 32 C300 60 600 10 800 10 C980 10 1100 24 1200 14" fill="none" stroke="#e9672a" stroke-width="7"/>
</svg>

<div class="abs top-bar">
  <span class="abs lic"><em>LIC No:</em> EC-4821</span>
  <span class="abs divider"></span>
  <span class="abs abn"><em>ABN:</em> 90 123 456 789</span>
</div>
<div class="abs top-phone">
  <svg width="14" height="14" viewBox="0 0 24 24"><path fill="#fff" d="M6.6 10.8a15 15 0 0 0 6.6 6.6l2.2-2.2a1 1 0 0 1 1-.25 11.4 11.4 0 0 0 3.6.6 1 1 0 0 1 1 1V20a1 1 0 0 1-1 1A17 17 0 0 1 3 4a1 1 0 0 1 1-1h3.5a1 1 0 0 1 1 1c0 1.25.2 2.45.6 3.6a1 1 0 0 1-.25 1z"/></svg>
  555.018.2040
</div>

<div class="abs header"></div>
<div class="abs brand"><span class="dot"></span>VOLTWISE ELECTRICAL</div>
<nav class="abs nav">
  <span class="active" style="width:68px">Home</span>
  <span style="width:20px;color:#999">|</span>
  <span style="width:130px">Our Services</span>
  <span style="width:148px">Meet Our Team</span>
  <span style="width:98px">Projects</span>
  <span>Contact Us</span>
</nav>

<div class="abs hero-title">We Provide A Trustworthy,<br>Reliable, And Professional<br>Team of Qualified Electricians</div>
<div class="abs hero-cta"><span class="mini-dot"></span>Contact Us Today</div>

<div class="abs hero-arrow" style="left:2px"><svg width="10" height="12" viewBox="0 0 10 12"><path d="M8 1 3 6l5 5" stroke="#fff" stroke-width="2.5" fill="none"/></svg></div>
<div class="abs hero-arrow" style="left:1164px"><svg width="10" height="12" viewBox="0 0 10 12"><path d="M2 1l5 5-5 5" stroke="#fff" stroke-width="2.5" fill="none"/></svg></div>

<!-- welcome -->
<h1 class="abs welcome-title head-font">WELCOME</h1>
<p class="abs welcome-text">Lorem ipsum dolor sit amet, consectetuer adipiscing elit, sed diam onummy nibh euismod tincidunt ut laoreet dolore magna aliquam erat volutpat. Ut wisi enim ad minim veniam, quis nostrud exerci tation ullamcorper suscipit lobortis nisl ut aliquip ex ea commodo consequat. Duis autem vel eum iriure dolor in hendrerit in vulputate velit esse molestie consequat, vel illum dolore eu feugiat nulla facilisis at vero eros et accumsan et iusto odio dignissim qui blandit praesent luptatum zzril delenit augue duis dolore te.</p>
<div class="abs pill"><span class="mini-dot"></span>Contact Us Today</div>
<div class="abs welcome-visual" role="img" aria-label="Circular photo of electricians at work"></div>

<!-- audience cards -->
<div class="abs card" style="left:149px">
  <div class="photo" role="img" aria-label="Suburban house lit at dusk" style="background:linear-gradient(180deg,#27418a 0%,#3a4c76 55%,#8a6a4a 100%)"></div>
  <div class="body" style="background:var(--navy)">
    <svg width="60" height="54" viewBox="0 0 60 54"><path d="M8 26 30 6l22 20" fill="none" stroke="#e9672a" stroke-width="5"/><path d="M14 24v24h32V24" fill="none" stroke="#e9672a" stroke-width="5"/><rect x="25" y="30" width="10" height="18" fill="#e9672a"/></svg>
    <h3 style="color:var(--orange)">Residential</h3>
    <p>Lorem ipsum dolorsectetuer adipiscing elit, sed dinonummy nibh euismod tincidut.</p>
  </div>
</div>
<div class="abs card" style="left:610px">
  <div class="body" style="background:var(--orange)">
    <svg width="60" height="54" viewBox="0 0 60 54"><rect x="12" y="14" width="16" height="36" fill="none" stroke="#1c2f5e" stroke-width="4"/><rect x="30" y="4" width="18" height="46" fill="none" stroke="#1c2f5e" stroke-width="4"/><path d="M6 50h48" stroke="#1c2f5e" stroke-width="4"/></svg>
    <h3 style="color:var(--navy)">Commerical</h3>
    <p>Lorem ipsum dolorsectetuer adipiscing elit, sed dinonummy nibh euismod tincidut.</p>
  </div>
  <div class="photo" role="img" aria-label="Office corridor with ceiling downlights" style="background:linear-gradient(180deg,#d8d9df 0%,#8d8fa0 50%,#3d4a80 100%)"></div>
</div>
<div class="abs card-badge"></div>

<!-- projects -->
<div class="abs projects"></div>
<h2 class="abs section-title" style="top:1282px;font-size:28px;color:var(--white)">PROJECTS <span style="color:var(--orange)">GALLERY</span></h2>
<div class="abs filters"><span class="on">All</span><span>Domestic</span><span>Commercial</span><span>Others</span></div>
<div class="abs tile" style="left:144px;background:linear-gradient(180deg,#dfe3e8,#7b8290)" role="img" aria-label="Warehouse with high bay lighting"><div class="cap">Lorem Ipsum Dolor</div></div>
<div class="abs tile" style="left:376px;background:linear-gradient(180deg,#eef0f2,#8a9aa8)" role="img" aria-label="Open office with panel lighting"><div class="cap">Lorem Ipsum Dolor</div></div>
<div class="abs tile" style="left:608px;background:linear-gradient(180deg,#3a2a1a,#9a6a3a)" role="img" aria-label="Dining room with pendant lamp"><div class="cap">Lorem Ipsum Dolor</div></div>
<div class="abs tile" style="left:841px;background:linear-gradient(180deg,#4a3a30,#b89a7a)" role="img" aria-label="Boardroom with decorative ceiling lights"><div class="cap">Lorem Ipsum Dolor</div></div>

<!-- testimonial -->
<div class="abs review"></div>
<div class="abs reviewer" role="img" aria-label="Portrait of a satisfied customer"></div>
<svg class="abs" style="left:408px;top:1702px" width="78" height="64" viewBox="0 0 78 64"><path d="M0 64V32C0 12 10 2 32 0v12C20 14 16 20 16 30h16v34zM44 64V32C44 12 54 2 76 0v12C64 14 60 20 60 30h16v34z" fill="#ececec"/></svg>
<p class="abs quote-text">Lorem ipsum dolor sit amet, consectetuer adipiscing elit, sed diam nonummy nibh euismod tincidunt ut laoreet dolore magna aliquam erat volutpat</p>
<div class="abs quote-name">Lorem Isopume</div>
<div class="abs round-arrow" style="left:173px"><svg width="8" height="10" viewBox="0 0 8 10"><path d="M6 0v10L0 5z" fill="#bbb"/></svg></div>
<div class="abs round-arrow" style="left:991px"><svg width="8" height="10" viewBox="0 0 8 10"><path d="M2 0v10l6-5z" fill="#bbb"/></svg></div>
<div class="abs more-link">Read More Reviews + Success Stories
  <svg width="26" height="10" viewBox="0 0 26 10"><path d="M0 5h24M19 1l5 4-5 4" stroke="#e9672a" stroke-width="1.6" fill="none"/></svg>
</div>

<!-- why choose us -->
<div class="abs why"></div>
<h2 class="abs section-title" style="top:2038px;font-size:35px;color:var(--navy)"><span style="color:var(--orange)">WHY</span> CHOOSE US</h2>
<p class="abs why-copy" style="top:2093px">Lighting design and application are paramount in our company's services.</p>
<p class="abs why-copy" style="top:2122px">Industry leading product use &amp; integration are always on the forefront with our customer client services.</p>
<div class="abs why-link"><span>SCHEDULE YOUR SERVICE TODAY</span></div>

<!-- footer -->
<div class="abs footer"></div>
<div class="abs col-title" style="left:145px;width:138px;color:#fff">Quick Links</div>
<div class="abs col-title" style="left:357px;width:183px;color:#fff">Contact Details</div>
<div class="abs col-title" style="left:624px;width:220px;color:#fff">Chirp Feeds</div>
<div class="abs" style="left:822px;top:2302px;width:22px;height:22px;border-radius:50%;background:var(--navy)"></div>

<div class="abs links" style="color:#fff">
  <div>›&nbsp; Home</div><div>›&nbsp; Our Services</div><div>›&nbsp; Meet Our Team</div><div>›&nbsp; Projects</div><div>›&nbsp; Contact Us</div>
</div>

<div class="abs" style="left:354px;top:2358px;color:#fff">
  <div class="contact-row"><svg width="14" height="18" viewBox="0 0 14 18"><path d="M7 0a7 7 0 0 0-7 7c0 5 7 11 7 11s7-6 7-11a7 7 0 0 0-7-7zm0 9.5A2.5 2.5 0 1 1 7 4.5a2.5 2.5 0 0 1 0 5z" fill="#1c2f5e"/></svg><span>Street Name, city Name<br>State Zipcode</span></div>
  <div class="contact-row" style="margin-top:18px"><svg width="16" height="14" viewBox="0 0 16 14"><rect x="0" y="1" width="16" height="12" fill="#1c2f5e"/><path d="M0 1l8 6 8-6" stroke="#e57441" stroke-width="1.5" fill="none"/></svg><span>hello@voltwise.test</span></div>
  <div class="contact-row" style="margin-top:20px"><svg width="15" height="15" viewBox="0 0 24 24"><path fill="#1c2f5e" d="M6.6 10.8a15 15 0 0 0 6.6 6.6l2.2-2.2a1 1 0 0 1 1-.25 11.4 11.4 0 0 0 3.6.6 1 1 0 0 1 1 1V20a1 1 0 0 1-1 1A17 17 0 0 1 3 4a1 1 0 0 1 1-1h3.5a1 1 0 0 1 1 1c0 1.25.2 2.45.6 3.6a1 1 0 0 1-.25 1z"/></svg><span>555.018.2041</span></div>
</div>

<div class="abs feed" style="color:#fff">
  <div style="display:flex;gap:10px;align-items:center;font-weight:600"><span style="width:10px;height:10px;border-radius:50%;background:var(--navy);display:inline-block"></span>Lorem um dolor sit onsectetue</div>
  <div style="margin-top:2px">Duis autem vel eum iriur dolor inndni rerit in vulputate velit esse molestie mo consequat, vel illum dolore facilisi. Lorem ipsum dummy text</div>
  <div style="margin-top:4px;font-weight:600;text-decoration:underline">View All</div>
</div>

<div class="abs footer-brand" style="color:#fff"><span class="dot"></span>VOLTWISE</div>

<div class="abs bottom-bar">
  <span class="abs" style="left:146px;top:14px">Copyright © 2019 Voltwise Electrical - All Rights Reserved.</span>
  <span class="abs social" style="left:986px"></span>
  <span class="abs social" style="left:1014px"></span>
  <span class="abs social" style="left:1043px"></span>
</div>

</body>
</html>
```